Logo and Business card design!

Welbrook Estates

We are a Property development and real estate company (needs a logo design).

Welbrook estates is based in Sydney Australia and will be dealing with high net worth individuals with a corporate background. The demographic of clients will be relatively youthful and savvy. We do development finance, property development and some portion of property sales

I'd like the 'Welbrook' part of the name to be strength of the title, with 'property' playing a very minor part, perhaps in tiny font somewhere off to the bottom or side or something

Thank you!

Target Market(s)

25-55 years old

Industry/Entity Type

Real Estate Development

Contact Information for Business Card

Please arrange this information as you see fit

Leon Brightwater
Managing Director
0417 582 273
leon@welbrookestates-example.com.au
www.welbrookestates-example.com.au

Logo Text

Welbrook estates

Font styles to use
Serif

Colors

Designer to choose colors to be used in the design.

Requirements
Must have
• PLEASE VIEW THE UPLOADED IMAGES AND EXAMPLES
• And please put 'property' in small letters at the bottom or to the side. I want it to play a minimalist role, with 'WELBROOK' being the feature
• Colours! Please make sure theyre mostly grey and white with possibly some other dark blue and maybe dark grey
Nice to have
• Please feel free to use whatever colors you like, the suggested colors are something I selected momentarily and dont necessarily reflect strict guidelines
Should not have
• NO pictures or shapes of houses. I dont want the logo design to be so literal in its imagery

```html
<!DOCTYPE html>
<html lang="en">
<head>
<meta charset="utf-8">
<title>Welbrook Estates — Business Card</title>
<link rel="stylesheet" href="https://fonts.googleapis.com/css2?family=Marcellus&family=Cinzel:wght@700&family=Open+Sans:wght@400&display=swap">
<style>
  :root {
    --page: #ecebe8;
    --card-dark: #0e0e0e;
    --card-light: #ffffff;
    --gold: #c8961a;
    --ink: #3d3d3d;
    --grey-soft: #2a2a2a;
  }
  * { box-sizing: border-box; margin: 0; padding: 0; }
  html, body { width: 1200px; height: 900px; overflow: hidden; }
  body { background: var(--page); position: relative; font-family: "Open Sans", sans-serif; }

  .card {
    position: absolute;
    width: 560px;
    height: 320px;
    border-radius: 3px;
    overflow: hidden;
    box-shadow: 0 6px 18px rgba(0,0,0,0.18);
  }

  /* Back of card */
  .card--back { left: 70px; top: 110px; background: var(--card-dark); }
  .card--back .pattern {
    position: absolute; inset: 0;
    background: radial-gradient(ellipse at 55% 45%, var(--grey-soft) 0%, var(--card-dark) 70%);
  }
  .card--back .wordmark {
    position: absolute; left: 0; right: 0; top: 118px;
    display: flex; align-items: center; justify-content: center; gap: 18px;
  }
  .mark-square { width: 34px; height: 34px; background: var(--gold); }

  .wordmark-text { font-family: "Marcellus", serif; font-weight: 400; color: var(--gold); text-align: center; line-height: 1; }
  .wordmark-text .name { display: block; font-size: 44px; letter-spacing: 1px; }
  .wordmark-text .sub { display: block; font-size: 13px; letter-spacing: 6px; margin-top: 6px; }

  /* Front of card */
  .card--front { left: 570px; top: 470px; background: var(--card-light); }
  .card--front .wordmark { position: absolute; left: 44px; top: 40px; }
  .card--front .band { position: absolute; left: 0; bottom: 0; }

  .person { position: absolute; left: 44px; top: 150px; }
  .person-name { font-family: "Cinzel", serif; font-weight: 700; font-size: 19px; color: var(--gold); letter-spacing: 0.5px; }
  .person-role { font-size: 14px; color: var(--ink); margin-top: 1px; }

  .contacts { position: absolute; left: 44px; top: 212px; list-style: none; }
  .contacts li { display: flex; align-items: center; gap: 9px; font-size: 14.5px; color: var(--ink); height: 22px; }
  .contacts svg { width: 13px; height: 13px; fill: var(--gold); flex: none; }
</style>
</head>
<body>

  <section class="card card--back" aria-label="Business card, back">
    <div class="pattern" role="img" aria-label="Faint dark skyline grid pattern"></div>
    <div class="wordmark">
      <span class="mark-square"></span>
      <span class="wordmark-text">
        <span class="name">WELBROOK</span>
        <span class="sub">ESTATES</span>
      </span>
    </div>
  </section>

  <section class="card card--front" aria-label="Business card, front">
    <div class="wordmark">
      <span class="wordmark-text">
        <span class="name">WELBROOK</span>
        <span class="sub">ESTATES</span>
      </span>
    </div>

    <div class="person">
      <p class="person-name">LEON BRIGHTWATER</p>
      <p class="person-role">Managing Director</p>
    </div>

    <ul class="contacts">
      <li>
        <svg viewBox="0 0 24 24"><path d="M6.6 10.8a15.1 15.1 0 0 0 6.6 6.6l2.2-2.2a1 1 0 0 1 1-.25 11.4 11.4 0 0 0 3.6.57 1 1 0 0 1 1 1V20a1 1 0 0 1-1 1A17 17 0 0 1 3 4a1 1 0 0 1 1-1h3.5a1 1 0 0 1 1 1c0 1.25.2 2.45.57 3.6a1 1 0 0 1-.25 1z"/></svg>
        0417 582 273
      </li>
      <li>
        <svg viewBox="0 0 24 24"><path d="M2 5h20v14H2z M3 6l9 7 9-7" stroke="#fff" stroke-width="1.5"/></svg>
        leon@welbrookestates-example.com.au
      </li>
      <li>
        <svg viewBox="0 0 24 24"><circle cx="12" cy="12" r="10"/><path d="M2 12h20M12 2c3 3 3 17 0 20M12 2c-3 3-3 17 0 20" stroke="#fff" stroke-width="1.5" fill="none"/></svg>
        www.welbrookestates-example.com.au
      </li>
    </ul>

    <svg class="band" width="560" height="90" viewBox="0 0 560 90" aria-hidden="true">
      <path d="M0 68 L400 68 Q440 68 450 30 L560 30 L560 90 L0 90 Z" fill="var(--gold)"/>
    </svg>
  </section>

</body>
</html>
```